IT company requires website redesign

I have an old boring website that I want to update - www.tlvx-example.com
I am a growing IT company beginning to look after more healthcare professionals such as medical and dental practices so a more professional look is required

Blue and orange are the company colours. See one of our local competitors for your reference and ideas - https://www.pixel-helpdesk.example.au

Target Market(s)

Medical, dental, professional, solicitors etc

Industry/Entity Type

It Support

Number of Pages Required

5+ page

Colors

Designer to choose colors to be used in the design.

Requirements
Must have
• Classy feel, simple with the 'less is more' approach
• On support page, links to support items, a couple more to come
• Reference to our technology partners
• Easy to read
Nice to have
• Company colours are blue with a little orange but I willing to consider new web colour schemes
• leave the rest to you

```html
<!DOCTYPE html>
<html lang="en">
<head>
<meta charset="utf-8">
<title>Clearpath Systems – IT Support</title>
<link href="https://fonts.googleapis.com/css2?family=Jost:wght@400;500;600&family=Open+Sans:ital,wght@0,400;0,600;0,700;1,400&family=Lora:ital,wght@1,500&display=swap" rel="stylesheet">
<style>
:root{
  --blue:#2b3990;
  --orange:#e8632b;
  --ink:#333;
  --muted:#777;
  --line:#d9d9d9;
  --pale:#f5f5f5;
  --nav-bg:#f7eeee;
  --footer:#0b0b0b;
  --white:#fff;
}
*{box-sizing:border-box;margin:0;padding:0}
html,body{width:1200px;height:3462px;overflow:hidden}
body{position:relative;background:var(--white);font-family:"Open Sans",Arial,sans-serif;color:var(--ink)}
.abs{position:absolute}
.section-title{position:absolute;left:0;width:1200px;text-align:center;font-family:"Jost",Arial,sans-serif;font-weight:600;font-size:31px;color:var(--blue)}
.section-title span{border-bottom:3px solid var(--blue);padding-bottom:2px}

/* header */
.site-header{top:0;left:0;width:1200px;height:81px}
.brand{left:95px;top:20px;display:flex;align-items:center;gap:10px;font-family:"Jost",sans-serif;font-weight:600;font-size:24px;color:var(--blue);line-height:1}
.brand i{width:14px;height:14px;border-radius:50%;background:var(--orange);display:block}
.contact-item{top:24px;display:flex;gap:8px;align-items:flex-start}
.contact-item b{display:block;font-family:"Jost",sans-serif;font-weight:500;font-size:18px;color:#222;line-height:1.1}
.contact-item small{display:block;font-size:10px;color:#999}
.main-nav{top:81px;left:0;width:1200px;height:62px;background:var(--nav-bg)}
.main-nav ul{list-style:none;position:absolute;left:95px;top:22px;display:flex;gap:38px}
.main-nav a{font-size:12px;font-weight:600;color:var(--blue);text-decoration:none}
.main-nav .current{border-bottom:2px solid var(--blue);padding-bottom:3px}

/* hero */
.hero{top:143px;left:0;width:1200px;height:457px;background:linear-gradient(135deg,#5a5650,#3b3a38 45%,#6e6a64 75%,#4a4744)}
.hero-copy{position:absolute;left:0;width:1200px;top:115px;text-align:center;color:var(--white)}
.hero-copy .welcome{font-family:"Jost",sans-serif;font-size:38px;font-weight:400}
.hero-copy h1{font-family:"Jost",sans-serif;font-size:58px;font-weight:600;line-height:1.05}
.hero-copy h1 em{font-style:normal;color:var(--orange)}
.hero-copy p{font-family:"Jost",sans-serif;font-size:21px;margin-top:6px}
.btn-ghost{display:inline-block;margin-top:30px;border:2px solid var(--white);padding:12px 28px;font-size:15px;font-weight:700;color:var(--white);text-decoration:none;letter-spacing:.5px}
.dots{position:absolute;top:397px;left:560px;display:flex;gap:8px}
.dots i{width:11px;height:11px;border-radius:50%;background:var(--white);display:block}
.dots i.on{background:var(--orange)}

/* about */
.about{top:600px;left:0;width:1200px;height:470px;background:#f7f7f7}
.col-title{font-size:15px;font-weight:700;color:var(--blue)}
.facts{position:absolute;left:95px;top:140px;width:520px;list-style:none}
.facts li{font-size:10.5px;color:#555;line-height:1.45;margin-bottom:9px;padding-left:11px;position:relative}
.facts li:before{content:"";position:absolute;left:0;top:4px;border-left:5px solid var(--orange);border-top:3.5px solid transparent;border-bottom:3.5px solid transparent}
.skills{position:absolute;left:665px;top:140px;width:442px}
.skill{margin-bottom:22px}
.skill p{font-size:10.5px;color:#666;margin-bottom:6px}
.bar{height:13px;border-radius:7px;background:#ddd;overflow:hidden}
.bar i{display:block;height:100%;border-radius:7px;background:var(--orange)}

/* services */
.services{top:1070px;left:0;width:1200px;height:740px}
.services .band{position:absolute;left:0;top:430px;width:1200px;height:310px;background:var(--pale)}
.card{position:absolute;width:232px;height:256px;background:var(--white);border:1px solid #ccc;text-align:center;padding:46px 18px 0}
.card svg{width:56px;height:56px}
.card h3{font-family:"Jost",sans-serif;font-size:15px;font-weight:600;color:var(--blue);margin-top:6px}
.card p{font-size:10px;color:#777;line-height:1.5;margin-top:4px}

/* team */
.team{top:1810px;left:0;width:1200px;height:422px;background:var(--pale)}
.team h2{position:absolute;left:95px;top:140px;font-family:"Jost",sans-serif;font-size:31px;font-weight:600;color:var(--blue);border-bottom:3px solid var(--blue);line-height:1.1}
.team-ctrl{position:absolute;top:215px;width:60px;height:45px;border:2px solid #222;background:var(--white);display:flex;align-items:center;justify-content:center}
.member{position:absolute;top:80px;width:226px;text-align:center}
.member .photo{width:226px;height:218px}
.member h4{font-size:13px;font-weight:600;color:var(--blue);margin-top:13px}
.member small{font-size:9.5px;color:var(--orange)}

/* testimonial */
.testimonial{top:2232px;left:0;width:1200px;height:386px}
.testimonial .photo{position:absolute;left:0;top:0;width:568px;height:386px;background:linear-gradient(120deg,#4a5a34,#2f3a24 50%,#7c6a52)}
.testimonial .notch{position:absolute;left:530px;top:155px}
.quote{position:absolute;left:605px;top:40px;width:500px}
.quote .mark{font-family:"Lora",serif;font-size:80px;color:var(--orange);line-height:.8;font-style:normal}
.quote p{font-size:12.5px;font-style:italic;color:#555;line-height:1.75;margin-top:10px}
.quote cite{display:block;margin-top:14px;font-family:"Lora",serif;font-size:22px;color:var(--orange)}

/* call to action */
.cta{top:2618px;left:0;width:1200px;height:164px;background:#efefef}
.cta h2{position:absolute;left:95px;top:50px;font-family:"Jost",sans-serif;font-weight:600;font-size:29px;color:var(--blue)}
.cta p{position:absolute;left:98px;top:92px;font-family:"Jost",sans-serif;font-size:19px;color:#444}
.btn-solid{position:absolute;left:893px;top:55px;width:214px;height:56px;background:var(--orange);color:var(--white);font-size:18px;font-weight:700;display:flex;align-items:center;justify-content:center;text-decoration:none}

/* partners */
.partners{top:2782px;left:0;width:1200px;height:338px}
.carousel{position:absolute;left:95px;top:135px;width:1012px;height:162px;border-top:1px solid #e3e3e3;border-bottom:1px solid #e3e3e3}
.slot{position:absolute;top:0;width:180px;height:160px;border-left:1px solid #e3e3e3;border-right:1px solid #e3e3e3;display:flex;align-items:center;justify-content:center}
.badge{width:118px;height:84px}
.carousel .arrow{position:absolute;top:62px}

/* footer */
.site-footer{top:3120px;left:0;width:1200px;height:342px;background:var(--footer);color:var(--white)}
.foot-brand{left:95px;top:30px;display:flex;align-items:center;gap:10px;font-family:"Jost",sans-serif;font-weight:600;font-size:22px;color:var(--white)}
.foot-brand i{width:12px;height:12px;border-radius:50%;background:var(--white);display:block}
.social{position:absolute;left:95px;top:130px;display:flex;gap:8px}
.social i{width:38px;height:38px;border-radius:50%;background:var(--white);display:block}
.foot-col{position:absolute;top:34px}
.foot-col h5{font-family:"Jost",sans-serif;font-weight:600;font-size:16px;margin-bottom:18px}
.foot-col li{list-style:none;font-size:10.5px;margin-bottom:14px;color:#eee}
.addr{display:flex;gap:10px;font-size:10.5px;line-height:1.5;margin-bottom:16px}
.addr svg{flex:none;margin-top:2px}
.field{width:214px;height:30px;background:var(--white);font-size:10px;color:#aaa;padding:9px 10px}
.submit{margin-top:8px;width:70px;height:24px;background:var(--orange);font-size:10px;font-weight:600;display:flex;align-items:center;justify-content:center}
.copyright{position:absolute;left:0;top:280px;width:1200px;text-align:center;font-size:10.5px;color:#ddd}
</style>
</head>
<body>

<header class="abs site-header">
  <div class="abs brand"><i></i>Clearpath Systems</div>
  <div class="abs contact-item" style="left:665px">
    <svg width="16" height="22" viewBox="0 0 16 22"><path d="M4 1 L7 6 L5 8 Q6 13 10 16 L12 14 L15 18 L12 21 Q1 16 1 4 Z" fill="#222"/></svg>
    <div><b>1300 000 482</b><small>Help Specialist Calling</small></div>
  </div>
  <div class="abs contact-item" style="left:822px">
    <svg width="16" height="22" viewBox="0 0 16 22"><path d="M8 1 A7 7 0 0 1 15 8 C15 13 8 21 8 21 C8 21 1 13 1 8 A7 7 0 0 1 8 1 Z" fill="#222"/><circle cx="8" cy="8" r="2.6" fill="#fff"/></svg>
    <div><b>12 Harbour Lane, Coastview QLD 4000</b><small>Gold Coast Service Location</small></div>
  </div>
</header>

<nav class="abs main-nav">
  <ul>
    <li><a class="current" href="#">Home</a></li>
    <li><a href="#">Our Services</a></li>
    <li><a href="#">About Us</a></li>
    <li><a href="#">Our Team</a></li>
    <li><a href="#">Contact Us</a></li>
    <li><a href="#">Support</a></li>
  </ul>
  <svg class="abs" style="left:1090px;top:23px" width="16" height="16" viewBox="0 0 16 16"><circle cx="6.5" cy="6.5" r="5" fill="none" stroke="#2b3990" stroke-width="1.6"/><path d="M10 10 L14.5 14.5" stroke="#2b3990" stroke-width="1.8"/></svg>
</nav>

<section class="abs hero" role="img" aria-label="Desk with laptops, tablets and business charts seen from above">
  <div class="hero-copy">
    <div class="welcome">Welcome to</div>
    <h1><em>Clearpath</em> Systems!</h1>
    <p>A Better Tomorrow, Through Intelligent use of Technology Today!</p>
    <a class="btn-ghost" href="#">READ MORE</a>
  </div>
  <div class="dots"><i></i><i></i><i></i><i class="on"></i><i></i></div>
</section>

<section class="abs about">
  <h2 class="section-title" style="top:50px"><span>About Us</span></h2>
  <h3 class="col-title abs" style="left:95px;top:137px">About Clearpath Systems</h3>
  <ul class="facts" style="top:175px">
    <li>Commenced trading in 1996, the retail division was sold in 2002. That September Clearpath Systems was launched</li>
    <li>100% Australian owned and operated</li>
    <li>Gold Coast based company servicing south east Queensland with a 'We come to you' attitude</li>
    <li>Multi-disciplinary service provider for the computer industry</li>
    <li>Born out of the need for talented and local IT supply, support and services people with a</li>
    <li>complete understanding of the requirements &amp; peculiarities that is IT</li>
    <li>Support that does not end 5pm Friday night</li>
    <li>Collectively provide flexible, complete &amp; cost effective solutions</li>
  </ul>
  <h3 class="col-title abs" style="left:665px;top:137px">Our experience</h3>
  <div class="skills" style="top:180px">
    <div class="skill"><p>Desktop Support – 45 years</p><div class="bar"><i style="width:75%"></i></div></div>
    <div class="skill"><p>Server Management – 26 years</p><div class="bar"><i style="width:46%"></i></div></div>
    <div class="skill"><p>Software Installations – 40 years</p><div class="bar"><i style="width:62%"></i></div></div>
    <div class="skill"><p>Desktop Support – 45 years</p><div class="bar"><i style="width:68%"></i></div></div>
  </div>
</section>

<section class="abs services">
  <div class="band"></div>
  <h2 class="section-title" style="top:48px"><span>Our Services</span></h2>

  <div class="card" style="left:95px;top:133px">
    <svg viewBox="0 0 56 56" fill="none" stroke="#e8632b" stroke-width="2.5"><rect x="6" y="6" width="44" height="44" rx="3"/><rect x="15" y="6" width="22" height="13"/><circle cx="28" cy="35" r="8"/></svg>
    <h3>Software</h3><p>Clearpath Systems has the tools, capabilities and expertise to guide any organisation with their software requirements</p>
  </div>
  <div class="card" style="left:353px;top:133px">
    <svg viewBox="0 0 56 56" fill="none" stroke="#e8632b" stroke-width="2.5"><rect x="10" y="12" width="36" height="24" rx="2"/><path d="M3 40 H53 L49 45 H7 Z"/></svg>
    <h3>Products</h3><p>We will determine and provide appropriate products and services to address your technology requirements</p>
  </div>
  <div class="card" style="left:615px;top:133px">
    <svg viewBox="0 0 56 56" fill="none" stroke="#e8632b" stroke-width="2.5"><rect x="6" y="8" width="44" height="30" rx="2"/><path d="M22 38 L20 47 H36 L34 38 M16 47 H40"/></svg>
    <h3>Solutions</h3><p>A full range of IT Solutions, includes carefully selected IT Service Partners to minimize risk and improve continuity</p>
  </div>
  <div class="card" style="left:875px;top:133px">
    <svg viewBox="0 0 56 56" fill="none" stroke="#e8632b" stroke-width="2.5"><path d="M8 20 L30 8 L48 18 L26 30 Z"/><path d="M8 26 L26 36 L48 24 M8 32 L26 42 L48 30 M8 38 L26 48 L48 36"/></svg>
    <h3>Finance – Flexi Rent</h3><p>Concerned about your budget? We can help you with payment plan options.</p>
  </div>

  <div class="card" style="left:95px;top:420px">
    <svg viewBox="0 0 56 56" fill="none" stroke="#e8632b" stroke-width="2.5"><rect x="5" y="8" width="46" height="40" rx="2"/><path d="M5 16 H51"/><circle cx="24" cy="33" r="6"/><circle cx="38" cy="30" r="4"/></svg>
    <h3>Programming</h3><p>Electronic design manufacturing and microprocessor programming</p>
  </div>
  <div class="card" style="left:353px;top:420px">
    <svg viewBox="0 0 56 56" fill="none" stroke="#e8632b" stroke-width="2.5"><path d="M12 14 H30 L38 22 V50 H12 Z"/><path d="M20 6 H38 L46 14 V42"/></svg>
    <h3>Copiers</h3><p>B&amp;W Photocopiers &amp; RIP with full integration into networks for printing and scanning</p>
  </div>
  <div class="card" style="left:615px;top:420px">
    <svg viewBox="0 0 56 56" fill="none" stroke="#e8632b" stroke-width="2.5"><rect x="16" y="6" width="24" height="14"/><rect x="6" y="20" width="44" height="20" rx="2"/><rect x="16" y="34" width="24" height="14"/></svg>
    <h3>Printers &amp; Scanners</h3><p>Colour Copiers, print servers &amp; integration into networks for printing and scanning</p>
  </div>
  <div class="card" style="left:875px;top:420px">
    <svg viewBox="0 0 56 56" fill="none" stroke="#e8632b" stroke-width="2.5"><circle cx="28" cy="28" r="21"/><path d="M7 28 H49 M28 7 C18 18 18 38 28 49 M28 7 C38 18 38 38 28 49"/></svg>
    <h3>Web Hosting and Design</h3><p>Our team of specialized staff are ready and waiting to assist you with all your website design and hosting needs.</p>
  </div>
</section>

<section class="abs team">
  <h2>Our Team</h2>
  <div class="team-ctrl" style="left:95px"><svg width="26" height="18" viewBox="0 0 26 18" fill="none" stroke="#222" stroke-width="2"><rect x="1" y="1" width="24" height="16"/><path d="M1 1 L13 10 L25 1"/></svg></div>
  <div class="team-ctrl" style="left:168px"><svg width="14" height="22" viewBox="0 0 14 22"><path d="M12 2 L3 11 L12 20" fill="none" stroke="#222" stroke-width="3"/></svg></div>
  <div class="team-ctrl" style="left:241px"><svg width="14" height="22" viewBox="0 0 14 22"><path d="M2 2 L11 11 L2 20" fill="none" stroke="#222" stroke-width="3"/></svg></div>
  <div class="member" style="left:390px"><div class="photo" role="img" aria-label="Portrait of a smiling team member in glasses and a denim shirt" style="background:linear-gradient(160deg,#6f7f8f,#3f5b7a)"></div><h4>Darren Holt</h4><small>Senior Field Technician</small></div>
  <div class="member" style="left:637px"><div class="photo" role="img" aria-label="Portrait of a smiling team member on a light background" style="background:linear-gradient(160deg,#d9d3cc,#b59a84)"></div><h4>Kelly Morgan</h4><small>IT Business Strategist</small></div>
  <div class="member" style="left:882px"><div class="photo" role="img" aria-label="Portrait of a team member in sunglasses and a dark jacket" style="background:linear-gradient(160deg,#8a6a5a,#2c2a2a)"></div><h4>Lewis Brandt</h4><small>Business Machines</small></div>
</section>

<section class="abs testimonial">
  <div class="photo" role="img" aria-label="Portrait of a bearded client in front of green foliage"></div>
  <svg class="notch" width="40" height="80" viewBox="0 0 40 80"><path d="M40 0 L0 40 L40 80 Z" fill="#fff"/></svg>
  <blockquote class="quote">
    <div class="mark">&ldquo;</div>
    <p>Clearpath Systems have been our IT support company for over 10 years. So why do we stick with them? Because they are awesome!! Dean and his staff are consistently able to solve our many and varied problems. Whether we phone about server functionality, email capacity, software issues or IT security, Dean and the team are always able to provide a quick and efficient response, leaving us to get on with our business. Reliable, knowledgeable, cost effective - Clearpath Systems are an asset to our company and I cannot recommend them highly enough.</p>
    <cite>Rosalie</cite>
  </blockquote>
</section>

<section class="abs cta">
  <h2>Clearpath Systems – We are here to help you!</h2>
  <p>A Better Tomorrow, Through Intelligent use of Technology Today!</p>
  <a class="btn-solid" href="#">Contact us Now!</a>
</section>

<section class="abs partners">
  <h2 class="section-title" style="top:52px"><span>Some of our Partners</span></h2>
  <div class="carousel">
    <svg class="arrow" style="left:-45px" width="24" height="36" viewBox="0 0 24 36"><path d="M20 3 L5 18 L20 33" fill="none" stroke="#bbb" stroke-width="3"/></svg>
    <div class="slot" style="left:150px"><div class="badge" style="background:#1aa3e8"></div></div>
    <div class="slot" style="left:330px"><div class="badge" style="background:#e8e8ee"></div></div>
    <div class="slot" style="left:510px"><div class="badge" style="background:#f1e4e4"></div></div>
    <div class="slot" style="left:690px"><div class="badge" style="background:#1f4e9a;height:60px"></div></div>
    <svg class="arrow" style="left:1032px" width="24" height="36" viewBox="0 0 24 36"><path d="M4 3 L19 18 L4 33" fill="none" stroke="#bbb" stroke-width="3"/></svg>
  </div>
</section>

<footer class="abs site-footer">
  <div class="abs foot-brand"><i></i>Clearpath Systems</div>
  <div class="social"><i></i><i></i><i></i><i></i></div>
  <div class="foot-col" style="left:385px">
    <h5>Navegation</h5>
    <ul><li>Home</li><li>Our Services</li><li>About Us</li><li>Our Team</li><li>Contact Us</li><li>Support</li></ul>
  </div>
  <div class="foot-col" style="left:538px;width:200px">
    <h5>Contact Us</h5>
    <div class="addr"><svg width="12" height="16" viewBox="0 0 16 22"><path d="M8 1 A7 7 0 0 1 15 8 C15 13 8 21 8 21 C8 21 1 13 1 8 A7 7 0 0 1 8 1 Z" fill="#fff"/></svg><div>ADDRESS:<br>12 Harbour Lane, Coastview QLD 4000</div></div>
    <div class="addr"><svg width="12" height="16" viewBox="0 0 12 16"><rect x="1" y="1" width="10" height="14" rx="2" fill="none" stroke="#fff" stroke-width="1.6"/></svg><div>PHONE NUMBERS:<br>1300 000 482</div></div>
    <div class="addr"><svg width="14" height="12" viewBox="0 0 14 12"><rect x="1" y="1" width="12" height="10" fill="#fff"/><path d="M1 1 L7 6 L13 1" stroke="#000" fill="none"/></svg><div>EMAIL:<br>info@tlvx-example.com</div></div>
  </div>
  <div class="foot-col" style="left:757px">
    <h5>Services</h5>
    <ul><li>Software</li><li>Products</li><li>Solutions</li></ul>
  </div>
  <div class="foot-col" style="left:893px">
    <h5>Newsletter</h5>
    <div class="field">Email</div>
    <div class="submit">Submit</div>
  </div>
  <div class="copyright">© 2016 Clearpath Systems</div>
</footer>

</body>
</html>
```